India Export Business Card Design

We are a small company importing from India,
Antique furniture and textiles.
We would like a design with somthing of India in it.
IE: Camels, Tuk Tuks, People or maybe Taj Mahal.
Only one of the above suggestions, we do not want the card to be to busy.
We travel to India twice a year to get the product and then come home to New Zealand and sell it.
And must have our business name which is
Kestrel Trading Company
Nz phone no. 64 9 375 8162
Mobile 64 21 603 174
Email briony@kestreltrading.co.nz
Www.kestreltrading.co.nz

Also my name and position
Briony Calder
Director

Reason: I am awaiting for a design to come back with different colours. Many thanks

Target Market(s)

Indian heritage furniture and textiles in India also
New Zealand market for public to buy the goods that is bought in India

Industry/Entity Type

Travel

Contact Information for Business Card

Kestrel Trading Company
17b Orland Road
RD 5 Papakura 2417
Auckland
New Zealand
email address which will be associated to our new website
website once we have it assigned

Requirements
Must have
• Company name and region.
Phone numbers
My name and title.
Nice to have
• I would like the card to portray India and as i said before, I like the idea of camels in a line with ropes between them like an animation.
But happy to see what other suggestions there are.

```html
<!DOCTYPE html>
<html lang="en">
<head>
<meta charset="utf-8">
<title>Kestrel Trading Company – Business Card</title>
<link rel="stylesheet" href="https://fonts.googleapis.com/css2?family=Playfair+Display:wght@700&family=Pinyon+Script&family=Parisienne&display=swap">
<style>
  :root {
    --backdrop: #ece7e1;
    --card-white: #ffffff;
    --teal: #1d6f86;
    --teal-deep: #155a6e;
    --mustard: #c9a233;
    --ink: #2a2a2a;
    --ink-soft: #3d4a52;
    --sky-top: #1c5f7c;
    --sky-mid: #5d9ab0;
    --sunset: #f2a93b;
    --sunset-glow: #f7c65a;
    --ground: #2b1c12;
  }
  * { box-sizing: border-box; margin: 0; padding: 0; }
  html, body { width: 1200px; height: 761px; overflow: hidden; }
  body { background: var(--backdrop); position: relative; }

  .card {
    position: absolute;
    width: 520px;
    height: 340px;
    top: 210px;
    box-shadow: 0 6px 18px rgba(0,0,0,.18);
    overflow: hidden;
  }

  /* Front */
  .card--front { left: 50px; }
  .front-scene {
    position: absolute; inset: 0;
    background: linear-gradient(180deg,
      var(--sky-top) 0%, var(--sky-mid) 38%, #b9b27a 56%,
      var(--sunset-glow) 64%, var(--sunset) 70%, #8a4a1c 80%, var(--ground) 100%);
  }
  .front-text {
    position: absolute; left: 0; right: 0; top: 44px;
    text-align: center; color: var(--ink);
  }
  .company-line {
    display: flex; align-items: center; justify-content: center; gap: 14px;
  }
  .company-line .rule { width: 60px; height: 1px; background: var(--ink); }
  .company-name {
    font-family: "Playfair Display", Georgia, serif;
    font-weight: 700; font-size: 20px; letter-spacing: 1px;
  }
  .region {
    font-family: "Playfair Display", Georgia, serif;
    font-weight: 700; font-size: 12px; margin-top: 4px;
  }
  .person-name {
    font-family: "Pinyon Script", cursive;
    font-size: 36px; margin-top: 2px; line-height: 1.1;
  }
  .person-role {
    font-family: "Playfair Display", Georgia, serif;
    font-weight: 700; font-size: 13px; margin-top: 6px;
  }

  /* Back */
  .card--back { left: 630px; background: var(--card-white); }
  .back-shapes { position: absolute; inset: 0; }
  .back-text {
    position: absolute; left: 200px; top: 22px; right: 16px;
    font-family: "Parisienne", cursive; color: var(--ink-soft);
    font-size: 15px; line-height: 1.3;
  }
  .back-heading { color: var(--mustard); font-size: 22px; line-height: 1.2; }
  .back-block p { margin: 0; }
  .back-block + .back-block { margin-top: 6px; }
</style>
</head>
<body>

<section class="card card--front">
  <div class="front-scene" role="img" aria-label="Photograph of a line of camels with riders silhouetted against a desert sunset"></div>
  <div class="front-text">
    <div class="company-line">
      <span class="rule"></span>
      <span class="company-name">Kestrel Trading Company</span>
      <span class="rule"></span>
    </div>
    <div class="region">Auckland</div>
    <div class="person-name">Briony Calder</div>
    <div class="person-role">Director</div>
  </div>
</section>

<section class="card card--back">
  <svg class="back-shapes" width="520" height="340" viewBox="0 0 520 340">
    <polygon points="0,0 185,0 100,100 0,100" fill="var(--mustard)"/>
    <polygon points="0,100 100,100 45,236 0,236" fill="var(--teal)"/>
    <rect x="0" y="278" width="520" height="62" fill="var(--teal)"/>
    <rect x="0" y="236" width="520" height="44" fill="var(--teal-deep)" role="img" aria-label="Silhouette of a caravan of camels walking in a line"/>
  </svg>
  <div class="back-text">
    <div class="back-block">
      <p class="back-heading">Location</p>
      <p>Kestrel Trading Company</p>
      <p>17b Orland Road RD 5</p>
      <p>Papakura 2417 - Auckland, New Zealand</p>
    </div>
    <div class="back-block">
      <p class="back-heading">Contact</p>
      <p>New Zealand phone no. 64 9 375 8162</p>
      <p>Mobile: 64 21 603 174</p>
      <p>Email: briony@kestreltrading.co.nz</p>
      <p>Www.kestreltrading.co.nz</p>
    </div>
  </div>
</section>

</body>
</html>
```